New Business Card Design Project

I would like my card design to look exactly like the logo, design, layout, and print of the current attached file. The only change I would like made would be for the print to say THE KMW GROUP instead of THE HALLORAN GROUP. Basically, just replace his group name with my group name. I would also like the backgroud to be the same texture and color as the attached file. I love the dark blue lettering and house logo on the card.

I am completely open to the rest of the card design. I just want something clean and simple. Only basic contact info required on the card. Maybe just name: Kyle M Warrick and cell # 555.914.2087 and email kyle@orchidhomesagent.com

```html
<!DOCTYPE html>
<html lang="en">
<head>
<meta charset="UTF-8">
<title>Rudy's – Business Card</title>
<link href="https://fonts.googleapis.com/css2?family=Oswald:wght@600&family=Work+Sans:wght@400;500;600&display=swap" rel="stylesheet">
<style>
  :root {
    --backdrop: #2a2a2a;
    --card: #1b1b1b;
    --card-edge: #232323;
    --gloss-dark: #0c0c0c;
    --ink-light: #d4d4d4;
    --ink-mid: #8a8a8a;
    --divider: #4a4a4a;
  }
  * { margin: 0; padding: 0; box-sizing: border-box; }
  html, body {
    width: 1200px;
    height: 900px;
    overflow: hidden;
    background: var(--backdrop);
  }
  .canvas {
    position: relative;
    width: 1200px;
    height: 900px;
    display: flex;
    flex-direction: column;
    align-items: center;
    justify-content: center;
    gap: 40px;
  }
  .card {
    position: relative;
    width: 640px;
    height: 366px;
    background: linear-gradient(135deg, var(--card-edge), var(--card));
    box-shadow: 0 10px 30px rgba(0,0,0,0.45);
  }

  /* Front */
  .card-front {
    display: flex;
    align-items: center;
    justify-content: center;
  }
  .brand-name {
    font-family: "Work Sans", sans-serif;
    font-weight: 600;
    font-size: 72px;
    color: var(--ink-light);
    letter-spacing: 0.5px;
  }

  /* Back */
  .identity {
    position: absolute;
    left: 60px;
    top: 140px;
    width: 210px;
    text-align: right;
  }
  .person-name {
    font-family: "Oswald", sans-serif;
    font-weight: 600;
    font-size: 30px;
    letter-spacing: 2px;
    color: var(--gloss-dark);
    text-shadow: 0 1px 0 rgba(255,255,255,0.06);
    line-height: 1.1;
    white-space: nowrap;
  }
  .person-title {
    font-family: "Work Sans", sans-serif;
    font-size: 12px;
    letter-spacing: 1px;
    color: var(--gloss-dark);
    text-shadow: 0 1px 0 rgba(255,255,255,0.06);
    margin-right: 10px;
    margin-top: 2px;
  }
  .divider {
    position: absolute;
    left: 292px;
    top: 140px;
    width: 1px;
    height: 58px;
    background: var(--divider);
  }
  .contact-list {
    position: absolute;
    left: 314px;
    top: 138px;
    list-style: none;
    font-family: "Work Sans", sans-serif;
    font-size: 15px;
    color: var(--ink-light);
    letter-spacing: 0.4px;
  }
  .contact-list li {
    display: flex;
    align-items: center;
    gap: 12px;
    height: 21px;
  }
  .contact-icon {
    width: 11px;
    height: 11px;
    flex: none;
  }
  .group-name {
    position: absolute;
    right: 40px;
    bottom: 36px;
    font-family: "Work Sans", sans-serif;
    font-weight: 500;
    font-size: 26px;
    letter-spacing: 2px;
    color: var(--ink-light);
  }
</style>
</head>
<body>
<main class="canvas">
  <section class="card card-front">
    <span class="brand-name">Rudy's</span>
  </section>

  <section class="card card-back">
    <div class="identity">
      <p class="person-name">KYLE M WARRICK</p>
      <p class="person-title">CEO</p>
    </div>
    <div class="divider"></div>
    <ul class="contact-list">
      <li>
        <svg class="contact-icon" viewBox="0 0 12 12" aria-hidden="true">
          <path d="M2.5 1 L4.5 1 L5.2 3.5 L4 4.5 C4.7 6 6 7.3 7.5 8 L8.5 6.8 L11 7.5 L11 9.5 C11 10.3 10.3 11 9.5 11 C5 11 1 7 1 2.5 C1 1.7 1.7 1 2.5 1 Z" fill="var(--ink-mid)"/>
        </svg>
        555.914.2087
      </li>
      <li>
        <svg class="contact-icon" viewBox="0 0 12 12" aria-hidden="true">
          <rect x="1" y="2.5" width="10" height="7" fill="none" stroke="var(--ink-mid)" stroke-width="1.2"/>
          <path d="M1 2.5 L6 6.5 L11 2.5" fill="none" stroke="var(--ink-mid)" stroke-width="1.2"/>
        </svg>
        kyle@orchidhomesagent.com
      </li>
      <li>
        <svg class="contact-icon" viewBox="0 0 12 12" aria-hidden="true">
          <circle cx="6" cy="6" r="5" fill="none" stroke="var(--ink-mid)" stroke-width="1.1"/>
          <ellipse cx="6" cy="6" rx="2.2" ry="5" fill="none" stroke="var(--ink-mid)" stroke-width="1"/>
          <path d="M1 6 H11" stroke="var(--ink-mid)" stroke-width="1"/>
        </svg>
        www.rudysCustoms.com
      </li>
    </ul>
    <p class="group-name">THE KMW GROUP</p>
  </section>
</main>
</body>
</html>
```